Dr Mira Thalen, Orthopaedic Hand Surgeon

I am an orthopaedic hand surgeon and need business cards that reflect the surgery I do. I operate on bones, ligaments, tendons, and soft tissues. I can do microsurgery (surgery under an operating microscope) - including connecting ends of cut nerves and arteries in the fingers together. As an orthopaedic surgeon, I also fix fractures and manage orthopaedic trauma in the rest of the body. I favour black as a colour, and have some pictures of hand X-rays that you can use in the design, if you think that would look good (feel free to crop).
Updates

Hi all. Thank you for all your submissions so far. Please note that I have updated my project brief. I would like to emphasise that use of the logos that I have provided is optional, and if used, I would very much prefer the logo not to dominate the card, but add to the overall aesthetic of the card. Warm regards, Mira

Target Market(s)

Referring medical practitioners, hand therapists, patients

Industry/Entity Type

Healthcare

Contact Information for Business Card

Dr Mira Thalen
Orthopaedic Hand Surgeon
MBBS BSc (Med), MIntPH (Merit), FCWES (Ortho), FUPelV

Font styles to use
Serif

Colors

Designer to choose colors to be used in the design.

Requirements
Must have
• Space for:
• 2 addresses (a PO Box Address and a consulting suite address) - to be confirmed
• 1 phone number - to be confirmed
Nice to have
• Please choose one of the FCWES logos (I included 3 - colour, black reverse, and greyscale); if you include this in the design, IT SHOULD NOT DOMINATE THE CARD, but be smaller and more discreet.
• I have also attached the FUPelV logo (colour and greyscale); if you choose to include this in the design, IT SHOULD NOT DOMINATE THE CARD, but be smaller and more discreet.
• I would love to be able to update details on the card as time goes on, and thus would like to own the template for the card as well.
• Also I would love discussion with regard to any changes on the card, if I am not completely happy with the design, and would like to discuss things such as ease of printing, finish on the cards (matte, polish) etc.
Should not have
• I don't like the card to look too crowded

```html
<!DOCTYPE html>
<html lang="en">
<head>
<meta charset="utf-8">
<title>Dr. Mira Thalen — Business Card</title>
<link href="https://fonts.googleapis.com/css2?family=Mulish:wght@700;800&family=Raleway:wght@300;400&display=swap" rel="stylesheet">
<style>
  :root {
    --backdrop: #ececec;
    --card: #fbfcfc;
    --ink-strong: #3b3f43;
    --ink-soft: #a3a6a9;
    --ink-faint: #b9bcbe;
    --mark: #8e9194;
  }
  html, body {
    margin: 0;
    width: 1200px;
    height: 1200px;
    overflow: hidden;
    background: var(--backdrop);
  }
  .canvas {
    position: relative;
    width: 1200px;
    height: 1200px;
    display: flex;
    align-items: center;
    justify-content: center;
  }
  .card {
    position: relative;
    width: 1000px;
    height: 571px;
    background: var(--card);
    box-shadow: 0 2px 10px rgba(0,0,0,0.08);
    font-family: "Raleway", sans-serif;
  }
  .credentials-marks {
    position: absolute;
    left: 70px;
    top: 250px;
    display: flex;
    align-items: center;
    gap: 22px;
  }
  .mark {
    display: flex;
    align-items: center;
    gap: 6px;
    font-family: "Raleway", sans-serif;
    font-weight: 400;
    font-size: 15px;
    color: var(--mark);
    letter-spacing: 0.02em;
  }
  .mark-square {
    width: 12px;
    height: 12px;
    background: var(--mark);
  }
  .identity {
    position: absolute;
    right: 60px;
    top: 120px;
    text-align: right;
  }
  .identity-name {
    margin: 0;
    font-family: "Mulish", sans-serif;
    font-weight: 800;
    font-size: 44px;
    color: var(--ink-strong);
    letter-spacing: 0.01em;
  }
  .identity-role {
    margin: 6px 0 0;
    font-weight: 300;
    font-size: 28px;
    color: var(--ink-soft);
    letter-spacing: 0.03em;
  }
  .identity-qualifications {
    margin: 8px 0 0;
    font-weight: 300;
    font-size: 14px;
    color: var(--ink-faint);
    letter-spacing: 0.02em;
  }
  .address {
    position: absolute;
    right: 60px;
    top: 300px;
    text-align: right;
  }
  .address-title {
    margin: 0 0 6px;
    font-family: "Mulish", sans-serif;
    font-weight: 700;
    font-size: 22px;
    color: var(--ink-strong);
  }
  .address-line {
    margin: 0;
    font-weight: 300;
    font-size: 20px;
    line-height: 1.45;
    color: var(--ink-soft);
    letter-spacing: 0.03em;
  }
  .contact {
    position: absolute;
    left: 70px;
    bottom: 60px;
    margin: 0;
    padding: 0;
    list-style: none;
  }
  .contact-item {
    font-weight: 300;
    font-size: 22px;
    line-height: 1.45;
    color: var(--ink-soft);
    letter-spacing: 0.03em;
  }
  .contact-label {
    font-family: "Mulish", sans-serif;
    font-weight: 800;
    color: var(--ink-strong);
  }
</style>
</head>
<body>
<main class="canvas">
  <section class="card">
    <div class="credentials-marks">
      <span class="mark"><span class="mark-square"></span>FUPelV</span>
      <span class="mark"><span class="mark-square"></span>FCWES</span>
    </div>

    <header class="identity">
      <h1 class="identity-name">Dr. Mira Thalen</h1>
      <p class="identity-role">Orthopaedic Hand Surgeon</p>
      <p class="identity-qualifications">MBBS BSc (Med), MIntPH (Merit), FCWES (Ortho), FUPelV</p>
    </header>

    <div class="address">
      <p class="address-title">Consulting Suite</p>
      <p class="address-line">Kemuning Baru 14</p>
      <p class="address-line">PO BOX 48210</p>
    </div>

    <ul class="contact">
      <li class="contact-item"><span class="contact-label">T</span> : +62 21 555 0184</li>
      <li class="contact-item"><span class="contact-label">M</span> : +62 821 5550 3921</li>
      <li class="contact-item"><span class="contact-label">E</span> : mira.thalen@example.com</li>
    </ul>
  </section>
</main>
</body>
</html>
```